Business card design needed for Automotive Reconditioning business

I have a logo design i just cant decide on the best color or layout for the business card, I will upload all the files so you can see all colors schemes we are considering. I have other file formats if needed let me know.

Target Market(s)

automotive dealerships

Contact Information for Business Card

HERE are the Descriptions and info needed on the card:
Interior Repair: Leather carpet burns panels dash Deoderize
Dealer products and Vin Verify
( spot for name and cell number) My name is Norman Bexley phone 614 352-4180 Title COO www.QuorvalMotive.com

Font styles to use
Sans Serif
Other font styles liked:
• what ever you think looks best

Requirements
Must have
• Must be able to change the name and phone for employees

```html
<!DOCTYPE html>
<html lang="en">
<head>
<meta charset="utf-8">
<title>Quorval Motive Reconditioning Corp. – Business Card</title>
<link href="https://fonts.googleapis.com/css2?family=Exo+2:wght@400;600;700&display=swap" rel="stylesheet">
<style>
  :root {
    --stage: #1e1b1c;
    --card: #2a2a2b;
    --card-light: #333334;
    --red: #e5401d;
    --blue: #1e9be0;
    --text-light: #e6e6e6;
    --text-muted: #cfcfcf;
  }
  * { box-sizing: border-box; margin: 0; padding: 0; }
  html, body {
    width: 1200px; height: 960px; overflow: hidden;
    background: var(--stage);
    font-family: "Exo 2", Arial, sans-serif;
  }
  .stage { position: relative; width: 1200px; height: 960px; }
  .card {
    position: absolute;
    width: 760px; height: 434px;
    background: radial-gradient(ellipse at 55% 50%, var(--card-light) 0%, var(--card) 70%);
    border-radius: 4px;
    box-shadow: 0 18px 40px rgba(0,0,0,.55);
    overflow: hidden;
  }
  .card--front { left: 110px; top: 40px; }
  .card--back { left: 330px; top: 490px; }

  .brand { display: flex; align-items: center; gap: 14px; }
  .brand__mark { width: 22px; height: 22px; background: var(--blue); flex: none; }
  .brand__name {
    color: var(--red); font-weight: 700; text-transform: uppercase;
    line-height: 1.05; letter-spacing: .5px;
  }
  .brand__name span { display: block; }

  .card--front .brand { position: absolute; left: 0; right: 0; top: 120px; justify-content: center; }
  .card--front .brand__name { font-size: 40px; }
  .card--front .brand__name .brand__sub { font-size: 21px; }

  .services {
    position: absolute; left: 0; right: 0; top: 270px;
    text-align: center; color: var(--text-muted);
    font-size: 19px; line-height: 1.3; font-weight: 400;
  }

  .person { position: absolute; left: 60px; top: 60px; }
  .person__name { color: var(--red); font-size: 34px; font-weight: 600; }
  .person__title { color: var(--blue); font-size: 24px; font-weight: 600; margin-top: 2px; }

  .contact { position: absolute; left: 60px; top: 300px; list-style: none; }
  .contact__item {
    display: flex; align-items: center; gap: 12px;
    color: var(--text-light); font-size: 24px; line-height: 1.35;
  }
  .contact__icon { width: 18px; height: 22px; flex: none; }

  .card--back .brand { position: absolute; right: 50px; top: 160px; }
  .card--back .brand__name { font-size: 36px; }
  .card--back .brand__name .brand__sub { font-size: 18px; }
</style>
</head>
<body>
<main class="stage">
  <section class="card card--front" aria-label="Card front">
    <div class="brand">
      <div class="brand__mark"></div>
      <div class="brand__name">
        <span>Quorval Motive</span>
        <span class="brand__sub">Reconditioning Corp.</span>
      </div>
    </div>
    <p class="services">Interior Repair : Leather carpet burns panels dash<br>Deoderize Dealer products and Vin Verify</p>
  </section>

  <section class="card card--back" aria-label="Card back">
    <div class="person">
      <p class="person__name">Norman Bexley</p>
      <p class="person__title">COO</p>
    </div>
    <ul class="contact">
      <li class="contact__item">
        <svg class="contact__icon" viewBox="0 0 18 22" aria-hidden="true">
          <path d="M4 2 L7 2 L8 7 L6 8.5 C7 12 9 14.5 11.5 16 L13 14 L17 15.5 L16.5 19 C10 20 2 12 2.5 4 Z" fill="var(--red)"/>
        </svg>
        <span>614 352-4180</span>
      </li>
      <li class="contact__item">
        <svg class="contact__icon" viewBox="0 0 18 22" aria-hidden="true">
          <rect x="4" y="1.5" width="11" height="19" rx="2" fill="none" stroke="var(--red)" stroke-width="2"/>
          <line x1="8" y1="17" x2="11" y2="17" stroke="var(--red)" stroke-width="2"/>
        </svg>
        <span>614 352-7731</span>
      </li>
    </ul>
    <div class="brand">
      <div class="brand__mark"></div>
      <div class="brand__name">
        <span>Quorval Motive</span>
        <span class="brand__sub">Reconditioning Corp.</span>
      </div>
    </div>
  </section>
</main>
</body>
</html>
```